ROVA Pty Ltd Business Card

Looking for a simple yet eye-catching double-sided business card design using my company logo on one side and contact details on the other.

Target Market(s)

Government

Industry/Entity Type

Communication Systems Engineering

Contact Information for Business Card

ROVA Pty Ltd

Requirements
Nice to have
• Would be great to have a QR code so details can be scanned into contacts

```html
<!DOCTYPE html>
<html lang="en">
<head>
<meta charset="utf-8">
<title>ROVA Pty Ltd Business Card</title>
<link rel="stylesheet" href="https://fonts.googleapis.com/css2?family=Roboto:wght@400;500;700;900&display=swap">
<style>
  :root {
    --backdrop: #e5e3e4;
    --card-light: #ffffff;
    --card-dark: #0a0b0a;
    --ink: #111111;
    --brand-slate: #2f3a40;
    --muted-light: #d9d9d9;
    --divider: #9a9a9a;
  }
  * { margin: 0; padding: 0; box-sizing: border-box; }
  html, body {
    width: 1189px; height: 1200px; overflow: hidden;
    background: var(--backdrop);
    font-family: "Roboto", Arial, sans-serif;
  }
  .canvas { position: relative; width: 1189px; height: 1200px; }
  .card {
    position: absolute; left: 273px; width: 643px; height: 368px;
    border-radius: 8px;
    box-shadow: 4px 6px 10px rgba(0,0,0,0.22);
    overflow: hidden;
  }
  .card--front { top: 215px; background: var(--card-light); color: var(--ink); }
  .card--back { top: 617px; background: var(--card-dark); color: var(--muted-light); }

  .brand { position: absolute; display: flex; align-items: center; }
  .brand__dot { border-radius: 50%; flex: none; }
  .brand__name { font-weight: 900; letter-spacing: 4px; line-height: 1; }

  .card--front .brand { left: 23px; top: 34px; }
  .card--front .brand__dot { width: 74px; height: 74px; background: var(--brand-slate); margin-right: 43px; }
  .card--front .brand__name { font-size: 60px; color: var(--brand-slate); }

  .address { position: absolute; left: 22px; top: 181px; font-size: 19.5px; line-height: 30.5px; }
  .contacts { position: absolute; left: 23px; top: 258px; list-style: none; }
  .contacts li { display: flex; align-items: center; height: 30px; font-size: 19.5px; }
  .contacts svg { width: 23px; height: 23px; margin-right: 12px; flex: none; }

  .divider { position: absolute; left: 350px; top: 190px; width: 1px; height: 153px; background: var(--divider); }

  .person { position: absolute; right: 23px; top: 234px; text-align: right; }
  .person__name { font-size: 30px; font-weight: 700; line-height: 38px; letter-spacing: 0.3px; }
  .person__role { font-size: 25px; font-weight: 400; line-height: 34px; }

  .card--back .brand { left: 150px; top: 58px; }
  .card--back .brand__dot { width: 80px; height: 80px; background: #ffffff; margin-right: 52px; }
  .card--back .brand__name { font-size: 66px; color: #ffffff; }

  .tagline {
    position: absolute; left: 132px; top: 184px; width: 380px; height: 51px;
    background: #ffffff; color: var(--ink); border-radius: 8px;
    display: flex; align-items: center; justify-content: center;
    font-size: 19.5px; font-weight: 700; letter-spacing: 0.2px;
  }
  .pitch { position: absolute; left: 22px; top: 242px; font-size: 18px; line-height: 28.5px; white-space: nowrap; }
  .pitch strong { color: #ffffff; font-weight: 700; }
</style>
</head>
<body>
<main class="canvas">
  <section class="card card--front" aria-label="Business card front">
    <div class="brand">
      <span class="brand__dot"></span>
      <span class="brand__name">ROVA</span>
    </div>

    <p class="address">14-16 Harlow Street&nbsp; Redfern<br>Vale NSW 2099 Australia</p>

    <ul class="contacts">
      <li>
        <svg viewBox="0 0 24 24" aria-hidden="true"><circle cx="12" cy="12" r="12" fill="#111"/><path d="M8 6.5c.6-.5 1.4-.4 1.8.2l1.1 1.8c.3.5.2 1.1-.2 1.5l-.8.7c.6 1.4 1.9 2.8 3.4 3.5l.7-.8c.4-.4 1-.5 1.5-.2l1.8 1.1c.6.4.7 1.2.2 1.8l-.8.9c-.8.8-2 1-3 .5-3-1.4-5.3-3.8-6.6-6.8-.4-1-.2-2.2.6-3z" fill="#fff"/></svg>
        000-000-0000
      </li>
      <li>
        <svg viewBox="0 0 24 24" aria-hidden="true"><circle cx="12" cy="12" r="12" fill="#111"/><rect x="5.5" y="7.5" width="13" height="9" rx="1" fill="none" stroke="#fff" stroke-width="1.6"/><path d="M5.8 8l6.2 5 6.2-5M5.8 16l4.6-4M18.2 16l-4.6-4" fill="none" stroke="#fff" stroke-width="1.4"/></svg>
        admin@rova.com.au
      </li>
      <li>
        <svg viewBox="0 0 24 24" aria-hidden="true"><circle cx="12" cy="12" r="12" fill="#111"/><g fill="none" stroke="#fff" stroke-width="1.2"><circle cx="12" cy="12" r="7"/><ellipse cx="12" cy="12" rx="3" ry="7"/><path d="M5 12h14M6 8.5h12M6 15.5h12"/></g></svg>
        https//rova.com.au
      </li>
    </ul>

    <div class="divider"></div>

    <div class="person">
      <p class="person__name">MARLEN AVERY</p>
      <p class="person__role">Co-Founder</p>
    </div>
  </section>

  <section class="card card--back" aria-label="Business card back">
    <div class="brand">
      <span class="brand__dot"></span>
      <span class="brand__name">ROVA</span>
    </div>

    <div class="tagline">SYESTEMS INTEGRATIONS SOLUTION</div>

    <p class="pitch">
      Let Us Solve Your Technical Issuses Through Our Knowledge And Experience<br>
      Of Systems Components And Engineering .<br>
      <strong>At ROVA</strong> we strive to ensure your mission critical teams have relia-ble assur-<br>
      ed communications.
    </p>
  </section>
</main>
</body>
</html>
```